Webbanner-Design für Affiliate Marketing
Zielgruppe
Online-Shop für Kopfbedeckungen aller Art (Hüte, Mützen, Fascinator, Stirnbänder)
Design soll eine möglichst große Zielgruppe ansprechen (Hauptfokus: 18-34 Jahre). Also alle Online-Shopper mit einer Vorliebe für Hüte/ Mützen.
Aufgabenstellung
Insgesamt ein modernes, eingängiges und stilvolles Design. Nicht allzu verspielt oder zu unruhig. Fokus auf das Wesentliche.
Text: A Headwear for Everyone
B Hüte und Mützen, Top Auswahl, Kostenlose Lieferung
C Gut behütet durch den Winter
D Der Hut-Online-Shop
Das Lumo Vanta Logo soll mit eingebunden werden. Keine vorgegebene Platzierung, sprich dem Design anpassen.
Formate: (Breite x Höhe)
1. Full Banner - 468 x 60 Pixel, max. 40k Dateigröße
2. Medium Rectangle - 300 x 250 Pixel, max. 40k Dateigröße
3. Vertical Banner - 120 x 240 Pixel, max. 30k Dateigröße
4. Rectangle - 180 x 150 Pixel, max. 40k Dateigröße

```html
<!DOCTYPE html>
<html lang="de">
<head>
<meta charset="utf-8">
<title>Lumo Vanta – Webbanner</title>
<link rel="stylesheet" href="https://fonts.googleapis.com/css2?family=Oswald:wght@400;500;600&display=swap">
<style>
  :root {
    --red: #f2474b;
    --white: #ffffff;
    --ink: #3a3a3a;
    --night: #141012;
    --photo-dark: #2a1f1c;
    --photo-mid: #6b4a3b;
    --photo-warm: #a7765e;
    --backdrop: #f3f3f3;
  }
  * { box-sizing: border-box; margin: 0; padding: 0; }
  html, body {
    width: 1200px; height: 1028px; overflow: hidden;
    background: var(--backdrop);
    font-family: "Oswald", "Arial Narrow", sans-serif;
  }
  .stage {
    position: absolute; left: 0; top: 17px;
    width: 816px; height: 676px;
    transform: scale(1.4706); transform-origin: 0 0;
  }
  .banner {
    position: absolute; overflow: hidden;
    background: var(--night); color: var(--white);
    box-shadow: 0 2px 8px rgba(0,0,0,.18);
  }
  .banner__photo {
    position: absolute; inset: 0;
    background:
      radial-gradient(ellipse 45% 70% at 78% 55%, var(--photo-warm) 0%, var(--photo-mid) 40%, transparent 75%),
      radial-gradient(ellipse 30% 40% at 35% 50%, var(--photo-mid) 0%, transparent 70%),
      linear-gradient(90deg, var(--photo-dark), #3b2b25 60%, var(--night));
  }
  .banner__shade {
    position: absolute; inset: 0;
    background: linear-gradient(180deg, transparent 55%, rgba(0,0,0,.75) 100%);
  }
  .brand {
    position: absolute; top: 0; left: 0; background: var(--white);
    display: flex; align-items: center; justify-content: center; gap: 5px;
  }
  .brand__dot { border-radius: 50%; background: var(--red); flex: none; }
  .brand__name { color: var(--ink); font-weight: 500; letter-spacing: .08em; white-space: nowrap; }
  .tag {
    position: absolute; left: 0; background: var(--red); color: var(--white);
    font-weight: 400; letter-spacing: .03em; white-space: nowrap;
    display: flex; align-items: center;
    clip-path: polygon(0 0, calc(100% - 7px) 0, 100% 50%, calc(100% - 7px) 100%, 0 100%);
  }
  .headline { position: absolute; line-height: 1; }
  .headline__main { display: block; font-weight: 500; text-transform: uppercase; }
  .headline__sub { display: block; font-weight: 400; }
  .benefits { position: absolute; list-style: none; line-height: 1.22; }
  .benefits li { position: relative; }
  .benefits li::before {
    content: ""; position: absolute; left: -8px; top: 50%;
    width: 4px; height: 6px; margin-top: -3px;
    background: var(--white); clip-path: polygon(0 0, 100% 50%, 0 100%);
  }
  .cta {
    position: absolute; background: var(--red); color: var(--white);
    display: flex; align-items: center; justify-content: center;
    font-weight: 500; text-transform: uppercase; white-space: nowrap;
  }
  .claim { position: absolute; font-weight: 400; white-space: nowrap; }

  /* Medium Rectangle 300 x 250 */
  .medium { left: 66px; top: 111px; width: 300px; height: 250px; }
  .medium .brand { width: 192px; height: 52px; }
  .medium .brand__dot { width: 16px; height: 16px; }
  .medium .brand__name { font-size: 20px; }
  .medium .tag { top: 52px; height: 22px; width: 152px; padding-left: 8px; font-size: 13px; }
  .medium .headline { left: 9px; top: 82px; }
  .medium .headline__main { font-size: 30px; }
  .medium .headline__sub { font-size: 16px; margin-top: 1px; }
  .medium .benefits { left: 18px; top: 166px; font-size: 13px; }
  .medium .cta { left: 154px; top: 207px; width: 140px; height: 33px; font-size: 22px; }
  .medium .claim { left: 10px; top: 228px; font-size: 10px; }

  /* Vertical Banner 120 x 240 */
  .vertical { left: 426px; top: 121px; width: 120px; height: 240px; }
  .vertical .brand { width: 120px; height: 30px; gap: 4px; }
  .vertical .brand__dot { width: 10px; height: 10px; }
  .vertical .brand__name { font-size: 12px; }
  .vertical .tag { top: 31px; height: 17px; width: 120px; padding-left: 4px; font-size: 10px; }
  .vertical .headline { left: 2px; top: 52px; }
  .vertical .headline__main { font-size: 22px; }
  .vertical .headline__sub { font-size: 12px; }
  .vertical .benefits { left: 15px; top: 160px; font-size: 9.5px; }
  .vertical .cta { left: 5px; top: 201px; width: 110px; height: 24px; font-size: 16px; }
  .vertical .claim { left: 14px; top: 228px; font-size: 7px; }

  /* Rectangle 180 x 150 */
  .rectangle { left: 64px; top: 392px; width: 180px; height: 150px; }
  .rectangle .brand { width: 110px; height: 26px; gap: 4px; }
  .rectangle .brand__dot { width: 10px; height: 10px; }
  .rectangle .brand__name { font-size: 12px; }
  .rectangle .tag { top: 26px; height: 15px; width: 120px; padding-left: 5px; font-size: 10px; }
  .rectangle .headline { left: 4px; top: 45px; }
  .rectangle .headline__main { font-size: 17px; }
  .rectangle .headline__sub { font-size: 10px; }
  .rectangle .benefits { left: 11px; top: 108px; font-size: 9.5px; }
  .rectangle .cta { left: 107px; top: 124px; width: 70px; height: 21px; font-size: 13.5px; }

  /* Full Banner 468 x 60 */
  .full { left: 289px; top: 392px; width: 468px; height: 60px; }
  .full .banner__photo {
    left: 140px;
    background:
      radial-gradient(ellipse 22% 90% at 75% 60%, var(--photo-warm) 0%, var(--photo-mid) 45%, transparent 80%),
      radial-gradient(ellipse 14% 80% at 40% 50%, var(--photo-mid) 0%, transparent 75%),
      linear-gradient(90deg, var(--night), #3b2b25 45%, var(--night));
  }
  .full .brand { width: 140px; height: 38px; gap: 5px; }
  .full .brand__dot { width: 12px; height: 12px; }
  .full .brand__name { font-size: 14px; }
  .full .brand-bg { position: absolute; left: 0; top: 0; width: 140px; height: 60px; background: var(--white); }
  .full .tag { top: 38px; height: 20px; width: 141px; padding-left: 6px; font-size: 12px; }
  .full .headline { left: 148px; top: 2px; }
  .full .headline__main { font-size: 16px; text-transform: none; }
  .full .headline__main span { text-transform: uppercase; }
  .full .headline__sub { font-weight: 400; }
  .full .benefits { left: 158px; top: 22px; font-size: 9.5px; line-height: 1.15; }
  .full .claim { right: 4px; top: 3px; font-size: 9px; text-align: right; line-height: 1.2; white-space: normal; width: 70px; }
  .full .cta { left: 383px; top: 36px; width: 82px; height: 20px; font-size: 14px; }
</style>
</head>
<body>
<main class="stage">

  <section class="banner medium" aria-label="Medium Rectangle 300 x 250">
    <div class="banner__photo" role="img" aria-label="Fotografie: junge Frau mit dunklem Hut mit gemustertem Hutband, im Hintergrund eine zweite Frau mit Hut"></div>
    <div class="banner__shade"></div>
    <div class="brand"><span class="brand__dot"></span><span class="brand__name">LUMO VANTA</span></div>
    <div class="tag">Der Hut-Online-Shop</div>
    <h2 class="headline"><span class="headline__main">A Headwear</span><span class="headline__sub">for Everyone</span></h2>
    <ul class="benefits"><li>Hüte und Mützen</li><li>Top Auswahl</li><li>Kostenlose Lieferung</li></ul>
    <p class="claim">Gut behütet durch den Winter</p>
    <a class="cta">Zum Shop</a>
  </section>

  <section class="banner vertical" aria-label="Vertical Banner 120 x 240">
    <div class="banner__photo" role="img" aria-label="Fotografie: junge Frau mit dunklem Hut, im Hintergrund eine zweite Frau mit Hut"></div>
    <div class="banner__shade"></div>
    <div class="brand"><span class="brand__dot"></span><span class="brand__name">LUMO VANTA</span></div>
    <div class="tag">Der Hut-Online-Shop</div>
    <h2 class="headline"><span class="headline__main">Headwear</span><span class="headline__sub">for Everyone</span></h2>
    <ul class="benefits"><li>Hüte und Mützen</li><li>Top Auswahl</li><li>Kostenlose Lieferung</li></ul>
    <a class="cta">Zum Shop</a>
    <p class="claim">Gut behütet durch den Winter</p>
  </section>

  <section class="banner rectangle" aria-label="Rectangle 180 x 150">
    <div class="banner__photo" role="img" aria-label="Fotografie: junge Frau mit dunklem Hut mit gemustertem Hutband"></div>
    <div class="banner__shade"></div>
    <div class="brand"><span class="brand__dot"></span><span class="brand__name">LUMO VANTA</span></div>
    <div class="tag">Der Hut-Online-Shop</div>
    <h2 class="headline"><span class="headline__main">Headwear</span><span class="headline__sub">for Everyone</span></h2>
    <ul class="benefits"><li>Hüte und Mützen</li><li>Top Auswahl</li><li>Kostenlose Lieferung</li></ul>
    <a class="cta">Zum Shop</a>
  </section>

  <section class="banner full" aria-label="Full Banner 468 x 60">
    <div class="banner__photo" role="img" aria-label="Fotografie: zwei junge Frauen mit Hüten"></div>
    <div class="brand-bg"></div>
    <div class="brand"><span class="brand__dot"></span><span class="brand__name">LUMO VANTA</span></div>
    <div class="tag">Der Hut-Online-Shop</div>
    <h2 class="headline"><span class="headline__main"><span>Headwear</span> <span class="headline__sub" style="display:inline;text-transform:none">for Everyone</span></span></h2>
    <ul class="benefits"><li>Hüte und Mützen</li><li>Top Auswahl</li><li>Kostenlose Lieferung</li></ul>
    <p class="claim">Gut behütet durch den Winter</p>
    <a class="cta">Zum Shop</a>
  </section>

</main>
</body>
</html>
```